Business Card Design Project

i need a bussines car design
Veltra Clinical Hypnotherapy

Gordon Wexley
Psychotherapy & Hypnosis

64029381 /0427956120

back of the card appoinment space.

file was provided on a PDF, LOgo , use the blu colorsa as well , elegant, clear,

Target Market(s)

young professional, caucasian , young mothers.

Industry/Entity Type

Business

```html
<!DOCTYPE html>
<html lang="en">
<head>
<meta charset="utf-8">
<title>Veltra Hypnotherapy – Business Card</title>
<link rel="stylesheet" href="https://fonts.googleapis.com/css2?family=Didact+Gothic&display=swap">
<style>
  :root {
    --bg: #3a3a3c;
    --card: #ffffff;
    --blue: #1f78c1;
    --blue-light: #9ec6e8;
    --ink: #2b2b2b;
    --ink-soft: #444444;
    --photo-a: #e9e2d6;
    --photo-b: #c9b7a0;
    --badge: #8fbf5a;
  }
  * { margin: 0; padding: 0; box-sizing: border-box; }
  html, body { width: 1200px; height: 900px; overflow: hidden; }
  body {
    background: var(--bg);
    font-family: "Didact Gothic", "Century Gothic", sans-serif;
    color: var(--ink);
    position: relative;
  }
  .card {
    position: absolute;
    top: 302px;
    width: 513px;
    height: 295px;
    background: var(--card);
    border-radius: 18px;
    overflow: hidden;
    box-shadow: 0 6px 14px rgba(0,0,0,0.45);
  }
  .card--front { left: 73px; }
  .card--back { left: 616px; }

  .brand { position: absolute; display: flex; align-items: flex-start; }
  .brand__dot { border-radius: 50%; background: var(--blue); flex: none; }
  .brand__text { display: flex; flex-direction: column; }
  .brand__name { color: var(--blue); line-height: 1; white-space: nowrap; }
  .brand__rule { height: 1px; background: var(--blue); }
  .brand__url { color: var(--ink-soft); white-space: nowrap; }

  .card--front .brand { left: 32px; top: 38px; }
  .card--front .brand__dot { width: 56px; height: 56px; margin-right: 64px; margin-top: 2px; }
  .card--front .brand__name { font-size: 29px; padding-bottom: 5px; }
  .card--front .brand__url { font-size: 12.5px; letter-spacing: 1.6px; margin-top: 3px; }

  .card--back .brand { left: 42px; top: 26px; }
  .card--back .brand__dot { width: 40px; height: 40px; margin-right: 52px; margin-top: 4px; }
  .card--back .brand__name { font-size: 21px; padding-bottom: 3px; }
  .card--back .brand__url { font-size: 9.5px; letter-spacing: 1.2px; margin-top: 2px; }

  .person { position: absolute; left: 28px; top: 140px; }
  .person__name { color: var(--blue); font-size: 24px; font-weight: 400; line-height: 1.1; }
  .person__role { font-size: 15px; margin-top: 4px; }

  .contact { position: absolute; left: 30px; top: 224px; list-style: none; font-size: 14px; line-height: 18.5px; }
  .contact li { display: flex; align-items: center; gap: 6px; }
  .contact svg { width: 10px; height: 12px; fill: var(--blue); flex: none; }

  .badge { position: absolute; left: 240px; top: 238px; width: 40px; height: 40px; border-radius: 50%; background: var(--badge); border: 2px solid #d8d8d8; }

  .portrait {
    position: absolute; left: 305px; top: 102px; width: 208px; height: 193px;
    background: linear-gradient(160deg, var(--photo-a) 0%, var(--photo-b) 100%);
  }

  .slots { position: absolute; left: 42px; top: 90px; list-style: none; font-size: 16px; line-height: 27.5px; color: var(--ink); }
  .slots li { white-space: pre; }

  .notice { position: absolute; left: 42px; top: 238px; font-size: 10.5px; line-height: 12.5px; color: var(--ink-soft); }
  .registration { position: absolute; left: 42px; top: 264px; font-size: 12px; color: var(--ink-soft); }
</style>
</head>
<body>

<section class="card card--front">
  <div class="brand">
    <span class="brand__dot"></span>
    <div class="brand__text">
      <span class="brand__name">Veltra Hypnotherapy</span>
      <span class="brand__rule"></span>
      <span class="brand__url">www.veltraclinicalhypnotherapy.com.au</span>
    </div>
  </div>

  <div class="person">
    <h1 class="person__name">Gordon Wexley</h1>
    <p class="person__role">Psychotherapy &amp; Hypnosis</p>
  </div>

  <ul class="contact">
    <li><svg viewBox="0 0 10 12"><path d="M5 0a4 4 0 0 0-4 4c0 3 4 8 4 8s4-5 4-8a4 4 0 0 0-4-4zm0 5.6a1.6 1.6 0 1 1 0-3.2 1.6 1.6 0 0 1 0 3.2z"/></svg>148 Corvell Rd, Ashdale</li>
    <li><svg viewBox="0 0 10 12"><path d="M2 0.5l2 2.5-1 1.2c.6 1.6 1.6 2.8 3 3.6l1.1-1 2.4 2-1 2.4C4.5 11 1 6.5 0.6 2z"/></svg>0427 956 120</li>
    <li><svg viewBox="0 0 10 12"><path d="M2 0h6a1 1 0 0 1 1 1v10a1 1 0 0 1-1 1H2a1 1 0 0 1-1-1V1a1 1 0 0 1 1-1zm0.8 1.5v7.5h4.4V1.5zM5 9.8a.7.7 0 1 0 0 1.4.7.7 0 0 0 0-1.4z"/></svg>6402 9381</li>
  </ul>

  <span class="badge" aria-hidden="true"></span>

  <div class="portrait" role="img" aria-label="Portrait photograph of the therapist, smiling, in a light shirt"></div>
</section>

<section class="card card--back">
  <div class="brand">
    <span class="brand__dot"></span>
    <div class="brand__text">
      <span class="brand__name">Veltra Hypnotherapy</span>
      <span class="brand__rule"></span>
      <span class="brand__url">www.veltraclinicalhypnotherapy.com.au</span>
    </div>
  </div>

  <ol class="slots">
    <li>1. ____am/pm _________________ ___/____/____</li>
    <li>2. ____am/pm _________________ ___/____/____</li>
    <li>3. ____am/pm _________________ ___/____/____</li>
    <li>4. ____am/pm _________________ ___/____/____</li>
    <li>5. ____am/pm _________________ ___/____/____</li>
  </ol>

  <p class="notice">To reschedule your appointment, please SMS or phone 0427 956 120<br>at least 24 hours prior to your allocated time. Thank you.</p>
  <p class="registration">NHRA Registration No. NPM058214</p>
</section>

</body>
</html>
```